Client Centric Brochure for Investment Advisory Firm

We need a client centric firm brochure that not only spotlights the services we provide as a wealth and investment management firm but also the value our expertise and expierience brings. We would like see designs that use this particular color green (RGB-0,92,51) and variations. Shouldn't be limited to this color however and are open to other color schemes Looking for something clean and consise. The final design should communicate financial safety, growth and reaching investment goals. Attached are rudimentary designs we have created, our company logo, and other source material. You can also visit our website www.harlowbendpartners.com for more inspiration.

Target Market(s)

Age Range - 35-65, Gender - 70% male, 30% female, Those looking to secure their financial future through wealth management and investing.

Industry/Entity Type

Investment

Font styles to use
Serif
Sans Serif

Colors
00a990

Requirements
Must have
• Project must have some of the information that was provided in the source documents. It must exhibit the client centric nature we are trying to exude.

```html
<!DOCTYPE html>
<html lang="en">
<head>
<meta charset="utf-8">
<title>Harlow Bend Partners – Brochure Spread</title>
<link href="https://fonts.googleapis.com/css2?family=Cinzel:wght@400;600&family=Lato:wght@400;700&family=Archivo+Black&display=swap" rel="stylesheet">
<style>
:root{
  --teal:#00a990;
  --teal-dark:#009a83;
  --green:#005c33;
  --ink:#1f1f1f;
  --charcoal:#333333;
  --bar-grey:#7a7a7a;
  --paper:#ffffff;
  --canvas:#ffffff;
}
*{margin:0;padding:0;box-sizing:border-box}
html,body{width:1200px;height:807px;overflow:hidden;background:var(--canvas)}
.spread{position:relative;width:1200px;height:807px}
.page{position:absolute;top:81px;width:503px;height:642px;background:var(--paper);
  box-shadow:0 2px 14px rgba(0,0,0,.22);overflow:hidden}
.page--disclosures{left:77px}
.page--cover{left:623px}

.brand{position:absolute;left:0;right:0;display:flex;align-items:center;justify-content:center;gap:12px}
.brand__mark{width:26px;height:26px;background:var(--green)}
.brand__name{font-family:"Cinzel",serif;font-weight:400;font-size:27px;color:var(--ink);letter-spacing:.5px}

.hero-disclosures{position:absolute;left:0;top:0;width:503px;height:262px;
  background:linear-gradient(180deg,#3f5a3a 0%,#6f8a68 40%,#b9c6b6 72%,#ffffff 100%)}
.page--disclosures .brand{top:284px}
.disclosures__title{position:absolute;top:348px;left:0;right:0;text-align:center;
  font-family:"Cinzel",serif;font-weight:400;font-size:14.5px;color:var(--teal);letter-spacing:.6px}
.disclosures__body{position:absolute;top:390px;left:24px;width:455px;
  column-count:2;column-gap:14px;font-family:"Lato",sans-serif;font-size:7.4px;line-height:9.8px;
  color:var(--ink);text-align:justify}

.site{position:absolute;left:0;right:0;text-align:center;font-family:"Lato",sans-serif;font-weight:700;
  font-size:9.5px;letter-spacing:6px;color:var(--ink)}
.page--disclosures .site{top:581px}
.page--cover .site{top:579px}
.band{position:absolute;left:0;width:100%;bottom:0;background:var(--teal-dark)}
.page--disclosures .band{height:30px}
.page--cover .band{height:27px}

.page--cover .brand{top:46px}
.page--cover .brand__mark{width:34px;height:34px}
.page--cover .brand__name{font-size:33px}
.hero-cover{position:absolute;left:0;top:129px;width:503px;height:251px;
  background:linear-gradient(90deg,#dfe9ee 0%,#cdd3cf 40%,#b9b2a6 60%,#e8ecef 100%)}
.headline{position:absolute;left:0;right:0;top:420px;text-align:center}
.headline__lead{display:block;font-family:"Cinzel",serif;font-weight:600;font-size:27px;color:var(--teal);letter-spacing:1px;line-height:34px}
.headline__main{display:block;font-family:"Archivo Black",sans-serif;font-size:38px;color:var(--charcoal);line-height:42px;letter-spacing:.5px}
.values{position:absolute;left:0;top:523px;width:503px;height:24px;background:var(--bar-grey);
  display:flex;justify-content:center;gap:38px;align-items:center;
  font-family:"Lato",sans-serif;font-size:14px;color:#fff}
.values__item{display:flex;align-items:center;gap:4px}
.values__item svg{width:10px;height:10px}
.values__shadow{position:absolute;left:40px;top:547px;width:423px;height:8px;
  background:radial-gradient(ellipse at top,rgba(0,0,0,.18),rgba(0,0,0,0) 70%)}
</style>
</head>
<body>
<div class="spread">

  <section class="page page--disclosures">
    <div class="hero-disclosures" role="img" aria-label="Photo of a footbridge leading into a forest, fading to white"></div>
    <div class="brand"><span class="brand__mark"></span><span class="brand__name">Harlow Bend Partners</span></div>
    <h2 class="disclosures__title">DISCLOSURES RELATED TO HARLOW BEND PARTNERS LLC</h2>
    <div class="disclosures__body">
      <p>In general the ETF-based Harlow Bend Portfolios seek to outperform their benchmarks by raising and lowering asset class exposures, industry sector exposures, country exposures, currency exposures, and various alternative asset class exposures to anticipate relative price movements. To this end, the portfolios may utilize fixed income ETFs, U.S. equity ETFs, international ETFs, currency strategy ETFs, and alternative class ETFs (including real estate, commodities, hedge fund strategies, private equity strategies, and potentially others) to adjust exposures where appropriate. There are risks involved with investing in ETFs, including possible loss of money. Index-based ETFs are not actively managed. Actively managed ETFs do not necessarily seek to replicate the performance of a specified index. Both index-based and actively-managed ETFs are subject to risks similar to stocks, including those related to short selling and margin maintenance. In addition to the normal risks associated with investing, international investments may involve risk of capital loss from unfavorable fluctuation in currency values, from differences in generally accepted accounting principles, or from economic or political instability in other nations. Emerging markets and frontier markets involve heightened risks related to the same factors as well as increased volatility and lower trading volume. Investments in smaller companies, in narrowly focused sectors, and in individual foreign countries typically exhibit higher volatility. Real estate investments are subject to changes in economic conditions, credit risk and interest rate fluctuations. Commodity-related investments are speculative and involve a high degree of risk. Commodities markets have historically been extremely volatile, creating the potential for losses regardless of the length of time an investment is held. Bonds and bond funds will decrease in value as interest rates rise.</p>
    </div>
    <div class="site">www.harlowbendpartners.com</div>
    <div class="band"></div>
  </section>

  <section class="page page--cover">
    <div class="brand"><span class="brand__mark"></span><span class="brand__name">Harlow Bend Partners</span></div>
    <div class="hero-cover" role="img" aria-label="Photo of a confident advisor in a light suit with colleagues talking in a bright office"></div>
    <h1 class="headline">
      <span class="headline__lead">INVESTMENT STRATEGIES THAT</span>
      <span class="headline__main">MATCH YOUR GOALS</span>
    </h1>
    <div class="values">
      <span class="values__item"><svg viewBox="0 0 10 10"><rect x="1" y="3" width="8" height="4" fill="none" stroke="#fff"/></svg>Simple</span>
      <span class="values__item"><svg viewBox="0 0 10 10"><rect x="1.5" y="1.5" width="7" height="7" fill="none" stroke="#fff"/><path d="M3 5l1.5 1.5L7 3.5" fill="none" stroke="#fff"/></svg>Efficient</span>
      <span class="values__item"><svg viewBox="0 0 10 10"><circle cx="5" cy="3.5" r="2.5" fill="none" stroke="#fff"/><path d="M5 6v4" stroke="#fff"/></svg>Innovative</span>
    </div>
    <div class="values__shadow"></div>
    <div class="site">www.harlowbendpartners.com</div>
    <div class="band"></div>
  </section>

</div>
</body>
</html>
```